PowerPoint Template - Swiss Tech Venture Fund

We are creating a fund to invest in swiss tech startups. We are entrepreneurs and we are building a model where we will not only invest in the startups but also help them scale.

We need ASAP a powerpoint template design to start our work. In couple of months, we will also need a proper website (as the one we have today, dalq7.ch) is not branded enough and too lightweight in terms of content.

For the ppt, we need
A PowerPoint master template
Fully editable slides
Consistent typography, layout, and visual system

Regarding the design, couple of hints
- We are swiss-based so we have to “feel it” in the presentation (symbols, mountains, etc).
- We are focused on Trust and Security technology. So it needs to be reflected as well (icons, typo, etc)
- The design should be primarily aligned with our new logo (see attached). We have a temporary website, but it should not be treated as a final reference (dalq7.ch)
- The design needs to feel “professional” as we are talking to institutions but also being able to be present to innovative tech startups
- We like very much the work done for another company (https://www.pixelvantora.com/design/58190276). So maybe a modified version of this one.

Target Market(s)

Institutional investors

Industry/Entity Type

Investment

Other font styles liked:
• Light compatible with the logo

Requirements
Must have
• Pictures (and not cartoon-like design). Icons that match our brand (trust and security)

```html
<!DOCTYPE html>
<html lang="en">
<head>
<meta charset="utf-8">
<title>Dalq7 – Presentation Template</title>
<link rel="stylesheet" href="https://fonts.googleapis.com/css2?family=Poppins:wght@300;400;500;600;700;800&family=Montserrat:wght@400;500;600;700&display=swap">
<style>
:root{
  --canvas:#d6d6d2;
  --red:#e0121a;
  --ink:#1d1d1d;
  --dark:#262626;
  --char:#3a3a3a;
  --grey:#9b9b9b;
  --light:#f1f1f1;
  --white:#ffffff;
}
*{box-sizing:border-box}
html,body{margin:0;padding:0}
body{width:1200px;height:3026px;overflow:hidden;background:var(--canvas);font-family:"Montserrat",sans-serif;color:var(--ink)}
.slide{position:absolute;width:491px;height:275px;overflow:hidden;background:var(--white)}
.slide > *{position:absolute;margin:0}
.photo{display:block}
.logo{font-family:"Poppins",sans-serif;font-weight:600;font-size:10px;letter-spacing:.5px;color:var(--ink)}
.logo-corner{right:22px;top:20px}
.hero{font-family:"Poppins",sans-serif;font-weight:800;font-size:29px;line-height:1.22}
.title{font-family:"Poppins",sans-serif;font-weight:500;font-size:22px;line-height:1.15;color:var(--ink)}
.title em{font-style:normal;color:var(--red)}
.kicker{font-size:5px;font-weight:600;color:var(--ink)}
.head{font-size:4.5px;font-weight:700;letter-spacing:.6px;color:var(--ink);text-transform:uppercase}
.lorem{font-size:4px;line-height:1.6;color:var(--grey)}
.url{left:24px;bottom:16px;font-size:5px;font-weight:600;color:var(--ink)}
.pager{right:24px;bottom:12px;font-size:4.5px;line-height:1.6;color:#b8b8b8;text-align:left}
.pill{background:var(--red);color:#fff;font-size:5px;border-radius:10px;padding:4px 22px 4px 10px}
.pill::after{content:"";position:absolute;right:3px;top:2px;width:10px;height:10px;border-radius:50%;background:#fff}
.dots span{display:inline-block;width:6px;height:6px;border-radius:50%;border:1px solid #bbb;margin:0 3px}
.dots span.on{background:var(--red);border-color:var(--red)}
.btn{font-size:4.5px;letter-spacing:1.5px;font-weight:700;color:#fff;text-align:center;padding:7px 0}
.toc{font-size:4.5px;color:var(--ink);width:160px}
.toc div{display:flex;justify-content:space-between;height:19.8px}
.agenda-num{font-family:"Poppins",sans-serif;font-weight:300;font-size:22px;color:var(--red)}
.agenda-lbl{font-size:6px;font-weight:600;line-height:1.2}
.agenda-time{font-size:4px;color:var(--grey)}
table{border-collapse:collapse;font-size:4px;color:#9a9a9a;text-align:center}
.fin td,.fin th{height:15.5px;border-bottom:1px solid #ececec}
.fin th{background:var(--ink);color:#fff;font-weight:500;height:16px}
.fin td.rowlbl{background:var(--red);color:#fff}
.cash td,.cash th{height:14px;border:1px solid #e8e8e8}
.cash th{color:#fff;font-weight:600}
</style>
</head>
<body>

<!-- Row 1 -->
<section class="slide" style="left:116px;top:81px">
  <div class="photo" role="img" aria-label="Misty alpine peak under heavy clouds" style="inset:0;background:linear-gradient(120deg,#6a6e6c 0%,#3a3e3d 45%,#2a2d2c 75%,#4b4f4d 100%)"></div>
  <p style="left:20px;top:10px;font-size:5px;color:#fff">Dalq7</p>
  <p class="logo" style="left:50px;top:40px;font-size:28px;color:#fff">DALQ7</p>
  <h1 class="hero" style="left:50px;top:94px;color:#fff">Accelerate the<br>Economy of Trust</h1>
  <p style="left:50px;top:177px;font-size:6.5px;color:#fff">Venture Capital for Deep Tech &amp; Trust-Based Innovation</p>
  <p style="left:50px;top:201px;font-size:6.5px;line-height:1.25;color:#fff;font-weight:600">Business<br>Presentation <span style="font-weight:400;color:#bbb">template.</span></p>
  <p style="left:50px;top:244px;font-size:4px;color:#fff">Modern Design</p>
  <p style="left:134px;top:234px;font-size:4px;line-height:1.3;color:#fff">Lorem ipsum<br>Dolor<br>Sit amet.</p>
  <div class="dots" style="left:229px;top:211px"><span></span><span class="on"></span><span></span></div>
  <svg style="right:34px;top:30px" width="14" height="10" viewBox="0 0 14 10"><path d="M0 1h14M0 5h14M0 9h14" stroke="#fff" stroke-width="1.3"/></svg>
  <svg style="right:36px;top:94px" width="10" height="6" viewBox="0 0 10 6"><path d="M1 5 5 1 9 5" fill="none" stroke="#ccc" stroke-width="1"/></svg>
  <svg style="right:38px;top:148px" width="6" height="12" viewBox="0 0 6 12"><rect x=".5" y=".5" width="5" height="11" rx="2.5" fill="none" stroke="#ccc"/></svg>
  <svg style="right:36px;top:214px" width="10" height="6" viewBox="0 0 10 6"><path d="M1 1 5 5 9 1" fill="none" stroke="#ccc" stroke-width="1"/></svg>
  <p style="right:16px;bottom:10px;font-size:5px;color:#fff;letter-spacing:.5px">TRUST <span style="display:inline-block;width:40px;border-top:1px solid #fff;vertical-align:middle;margin:0 6px"></span> ECONOMY</p>
</section>

<section class="slide" style="left:619px;top:81px">
  <p class="logo" style="left:42px;top:18px;font-size:19px">DALQ7</p>
  <p style="right:24px;top:20px;font-size:4px;font-weight:600">WWW.NORVALECAPITAL.COM</p>
  <div style="left:0;top:53px;width:300px;height:167px;background:var(--dark)"></div>
  <div style="left:300px;top:53px;width:9px;height:167px;background:var(--red)"></div>
  <div class="photo" role="img" aria-label="Two young colleagues working together in a creative studio" style="left:309px;top:53px;width:182px;height:167px;background:linear-gradient(135deg,#4a3a34,#b9875a 55%,#3c302a)"></div>
  <h1 class="hero" style="left:27px;top:92px;font-size:26px;color:#fff">Accelerate the<br>Economy of Trust</h1>
  <p style="left:27px;top:171px;font-size:6px;color:#fff">Venture Capital for Deep Tech &amp; Trust-Based Innovation</p>
  <p style="left:27px;top:191px;font-size:6px;line-height:1.2;color:#fff;font-weight:600">Business<br>Presentation<br><span style="font-weight:400;color:#aaa">template.</span></p>
  <p style="left:27px;top:229px;font-size:4px;color:#fff">Modern Design</p>
  <p style="left:108px;top:224px;font-size:4px;line-height:1.3;color:#fff">Lorem ipsum<br>Dolor<br>Sit amet.</p>
  <p class="pill" style="left:196px;top:210px">Explore More</p>
</section>

<!-- Row 2 -->
<section class="slide" style="left:116px;top:369px">
  <div class="photo" role="img" aria-label="Hiker in orange jacket and red beanie working on a laptop above snowy mountains" style="inset:0;background:linear-gradient(90deg,#c2794a 0%,#d9a27a 25%,#dfe5ea 50%,#ffffff 66%)"></div>
  <p class="logo" style="left:305px;top:28px;font-size:19px">DALQ7</p>
  <h1 class="hero" style="right:31px;top:67px;font-size:27px;color:var(--ink);text-align:right;line-height:1.22">Accelerate the<br>Economy of Trust</h1>
  <p style="right:48px;top:140px;font-size:6px;color:var(--red);font-weight:600">Venture Capital for Deep Tech &amp; Trust-Based Innovation</p>
  <p style="left:352px;top:173px;font-size:6px;line-height:1.2;font-weight:600">Business<br>Presentation <span style="font-weight:400;color:#999">template.</span></p>
  <p class="pill" style="left:378px;top:216px">Explore More</p>
  <p style="left:393px;top:236px;font-size:4.5px;font-weight:600">www.dalq7.ch</p>
</section>

<section class="slide" style="left:619px;top:369px;background:var(--dark)">
  <div class="photo" role="img" aria-label="Dim modern office interior" style="left:0;top:0;width:233px;height:275px;background:linear-gradient(160deg,#3c3c3c,#1e1e1e)"></div>
  <div style="left:233px;top:0;width:9px;height:275px;background:var(--red)"></div>
  <div style="left:242px;top:0;width:228px;height:275px;background:#fff"></div>
  <div class="photo" role="img" aria-label="Dark textured edge" style="left:470px;top:0;width:21px;height:275px;background:#2e2e2e"></div>
  <h1 style="left:27px;top:90px;font-family:Poppins,sans-serif;font-weight:600;font-size:34px;line-height:1.2;color:#fff;letter-spacing:1px">Table of<br>Contents</h1>
  <div class="toc" style="left:286px;top:41px">
    <div><span>ABOUT NORVALE</span><span>03</span></div>
    <div><span>VISION &amp; MISSION</span><span>04</span></div>
    <div><span>PROFESSIONAL TEAM</span><span>05</span></div>
    <div><span>OUR SERVICES</span><span>06</span></div>
    <div><span>SATISFIED CLIENTS</span><span>07</span></div>
    <div><span>FEATURED PROJECT</span><span>08</span></div>
    <div><span>PROJECT TIMELINE</span><span>09</span></div>
    <div><span>PRICING PLAN</span><span>10</span></div>
    <div><span>CLIENT TESTIMONIAL</span><span>11</span></div>
    <div><span>CONTACT INFO</span><span>12</span></div>
  </div>
  <p class="pager" style="right:54px">01 / 39<br>Welcome Slide</p>
</section>

<!-- Row 3 -->
<section class="slide" style="left:116px;top:657px">
  <div style="left:0;top:43px;width:34px;height:2px;background:#555"></div>
  <h2 class="title" style="left:58px;top:33px;font-size:18px">Presentation<br><em>Agenda</em></h2>
  <p class="logo logo-corner">DALQ7</p>
  <div style="left:58px;top:123px;width:2px;height:73px;background:var(--ink)"></div>
  <p class="agenda-num" style="left:80px;top:118px">01</p><p class="agenda-lbl" style="left:126px;top:124px">About<br>US</p><p class="agenda-time" style="left:126px;top:142px">From 08:00 to 09:00</p>
  <p class="agenda-num" style="left:216px;top:118px">02</p><p class="agenda-lbl" style="left:262px;top:124px">Who<br>We Are?</p><p class="agenda-time" style="left:262px;top:142px">From 09:00 to 10:00</p>
  <p class="agenda-num" style="left:353px;top:118px">03</p><p class="agenda-lbl" style="left:399px;top:124px">What<br>We DO?</p><p class="agenda-time" style="left:399px;top:142px">From 10:30 to 11:00</p>
  <p class="agenda-num" style="left:80px;top:170px">04</p><p class="agenda-lbl" style="left:126px;top:176px">Our<br>Works</p><p class="agenda-time" style="left:126px;top:194px">From 11:00 to 12:00</p>
  <p class="agenda-num" style="left:216px;top:170px">05</p><p class="agenda-lbl" style="left:262px;top:176px">Project<br>Timeline</p><p class="agenda-time" style="left:262px;top:194px">From 01:00 to 02:00</p>
  <p class="agenda-num" style="left:353px;top:170px">06</p><p class="agenda-lbl" style="left:399px;top:176px">Some<br>Analysis</p><p class="agenda-time" style="left:399px;top:194px">From 02:00 to 03:00</p>
  <p class="url">www.dalq7.ch</p>
  <p class="pager" style="right:26px">01 / 39<br>Welcome Slide</p>
</section>

<section class="slide" style="left:619px;top:657px">
  <p class="kicker" style="left:50px;top:28px">About Company</p>
  <h2 class="title" style="left:50px;top:42px">Who <em>We Are</em></h2>
  <div style="left:50px;top:86px;width:80px;height:2px;background:var(--ink)"></div>
  <p class="head" style="left:50px;top:104px">Text Tittle Here</p>
  <p class="lorem" style="left:50px;top:112px;width:135px">Our team backs founders with capital, guidance and a network that helps them scale across Europe.</p>
  <p class="head" style="left:50px;top:160px">Text Tittle Here</p>
  <p class="lorem" style="left:50px;top:168px;width:135px">We invest early in secure technology and stay close to every company as it grows.</p>
  <div style="left:0;top:230px;width:186px;height:45px;background:var(--red)"></div>
  <p style="left:24px;top:248px;font-size:5px;font-weight:600;color:#fff">www.dalq7.ch</p>
  <div style="left:186px;top:251px;width:124px;height:1px;background:var(--red)"></div>
  <div class="photo" role="img" aria-label="Red mountain train crossing a snowy alpine valley" style="left:186px;top:168px;width:124px;height:80px;background:linear-gradient(150deg,#9aa3a8,#e7ebee 50%,#8c2a22)"></div>
  <div style="left:244px;top:107px;width:67px;height:61px;background:#111"></div>
  <p style="left:258px;top:135px;font-size:4.5px;color:#fff;letter-spacing:1.5px;font-weight:700">TEXT TITTLE</p>
  <div class="photo" role="img" aria-label="Young man in brown leather jacket holding a sheet of paper" style="left:340px;top:0;width:151px;height:275px;background:linear-gradient(160deg,#cfcfcf,#7a5a44 55%,#c8c8c8)"></div>
  <p class="logo logo-corner" style="right:22px">DALQ7</p>
  <p class="pager" style="color:#eee">01 / 39<br>Welcome Slide</p>
</section>

<!-- Row 4 -->
<section class="slide" style="left:116px;top:945px">
  <div style="left:0;top:0;width:80px;height:275px;background:linear-gradient(180deg,#4a4a4a,#1f1f1f)"></div>
  <div class="photo" role="img" aria-label="Swiss flag waving in front of misty mountains" style="left:45px;top:34px;width:211px;height:201px;background:linear-gradient(140deg,#c6ccd0 0%,#d12a2c 40%,#b41d20 65%,#7d8f8a 100%)"></div>
  <p class="kicker" style="left:288px;top:36px">About Company</p>
  <h2 class="title" style="left:288px;top:52px">Our <em>Mission</em></h2>
  <div style="left:288px;top:90px;width:80px;height:2px;background:var(--ink)"></div>
  <p class="head" style="left:288px;top:117px">Text Tittle Here</p>
  <p class="lorem" style="left:288px;top:125px;width:145px">We fund founders who build trusted technology and help them scale with capital and experience.</p>
  <p class="head" style="left:288px;top:174px">Text Tittle Here</p>
  <p class="lorem" style="left:288px;top:182px;width:145px">Our mission is to grow a strong Swiss ecosystem for secure and deep tech ventures.</p>
  <p class="logo logo-corner">DALQ7</p>
  <p style="left:24px;top:254px;font-size:5px;font-weight:600;color:#fff">www.dalq7.ch</p>
  <div style="left:151px;top:235px;width:239px;height:40px;background:var(--red)"></div>
  <p style="left:199px;top:252px;font-size:4.5px;color:#fff">Text Tittle</p>
  <p style="left:254px;top:252px;font-size:4.5px;color:#fff">Text Tittle</p>
  <p style="left:309px;top:252px;font-size:4.5px;color:#fff">Text Tittle</p>
  <div style="left:390px;top:235px;width:101px;height:40px;background:#111"></div>
  <p style="left:429px;top:253px;font-size:4.5px;color:#fff;letter-spacing:1.5px;font-weight:700">TEXT TITTLE</p>
</section>

<section class="slide" style="left:619px;top:945px">
  <p class="kicker" style="left:37px;top:45px">About Company</p>
  <h2 class="title" style="left:37px;top:58px"><em>Why</em> DALQ7?</h2>
  <div style="left:37px;top:97px;width:80px;height:2px;background:var(--ink)"></div>
  <p class="head" style="left:37px;top:119px">Text Tittle Here</p>
  <p class="lorem" style="left:37px;top:127px;width:135px">We bring capital, hands-on support and a trusted network to every startup we back.</p>
  <p class="head" style="left:37px;top:178px">Text Tittle Here</p>
  <p class="lorem" style="left:37px;top:186px;width:135px">Our partners have built and scaled companies, so we know what founders need next.</p>
  <div style="left:202px;top:41px;width:40px;height:185px;background:var(--red)"></div>
  <p style="left:214px;top:47px;font-size:8px;color:#fff">+</p>
  <p style="left:218px;top:120px;font-size:4.5px;color:#fff;writing-mode:vertical-rl;letter-spacing:1px">LOREM IPSUM</p>
  <p style="left:212px;top:200px;font-size:8px;color:#fff">→</p>
  <div class="photo" role="img" aria-label="Team gathered around laptops in a loft office" style="left:242px;top:41px;width:229px;height:185px;background:linear-gradient(135deg,#6f6f6f,#c8c8c4 45%,#4a4a4a)"></div>
  <p class="logo logo-corner">DALQ7</p>
  <p class="pager">01 / 39<br>Welcome Slide</p>
</section>

<!-- Row 5 -->
<section class="slide" style="left:116px;top:1233px">
  <div style="left:121px;top:0;width:192px;height:52px;background:var(--red)"></div>
  <p style="left:147px;top:34px;font-size:4.5px;color:#fff">Text Tittle</p>
  <p style="left:202px;top:34px;font-size:4.5px;color:#fff">Text Tittle</p>
  <p style="left:272px;top:27px;font-size:11px;color:#fff">+</p>
  <div class="photo" role="img" aria-label="Glass office towers beside a tree-lined plaza" style="left:0;top:52px;width:312px;height:170px;background:linear-gradient(110deg,#4d5a66,#9fb0bc 45%,#6d9a3f 70%,#c9d5b8)"></div>
  <div style="left:0;top:222px;width:121px;height:53px;background:var(--dark)"></div>
  <p style="left:24px;top:253px;font-size:5px;font-weight:600;color:#fff">www.dalq7.ch</p>
  <p class="logo logo-corner">DALQ7</p>
  <p class="kicker" style="left:330px;top:44px">About Company</p>
  <h2 class="title" style="left:330px;top:55px">Investment<br><em>Focus</em></h2>
  <p class="head" style="left:340px;top:132px;width:40px">Text Tittle Here</p>
  <p class="lorem" style="left:340px;top:148px;width:70px">We focus on security, data trust and deep tech teams at seed and early growth stage.</p>
  <p style="left:340px;top:203px;font-size:5px;font-weight:600">Text Tittle  Here</p>
  <p style="left:340px;top:216px;font-size:4px;color:#555;font-style:italic;line-height:1.5">California, 03/14/1990<br>CEO &amp; Owner</p>
  <p class="pager">01 / 39<br>Welcome Slide</p>
</section>

<section class="slide" style="left:619px;top:1233px">
  <div class="photo" role="img" aria-label="Colleagues smiling in a bright meeting room" style="left:0;top:0;width:491px;height:122px;background:linear-gradient(90deg,#d4d1cc,#a6a29c 45%,#6c6660 75%,#c9c6c1)"></div>
  <p class="logo logo-corner">DALQ7</p>
  <div style="left:215px;top:90px;width:175px;height:32px;background:var(--red)"></div>
  <p style="left:262px;top:106px;font-size:4.5px;color:#fff">Text Tittle</p>
  <div style="left:300px;top:108px;width:60px;height:1px;background:#fff"></div>
  <div style="left:390px;top:90px;width:101px;height:108px;background:#111"></div>
  <p style="left:402px;top:108px;font-size:4.5px;color:#fff">2018 <span style="display:inline-block;width:32px;border-top:1px solid #fff;vertical-align:middle;margin:0 8px"></span> 2020</p>
  <p style="left:402px;top:130px;font-size:6.5px;color:#fff">Text Tittle Here</p>
  <p class="lorem" style="left:402px;top:144px;width:80px;color:#aaa">Growth of secure data platforms across the Swiss market.</p>
  <p class="kicker" style="left:50px;top:129px">About Company</p>
  <h2 class="title" style="left:50px;top:138px;font-size:16px">Trust Economy: Data &amp; Security</h2>
  <p class="head" style="left:50px;top:184px">Text Tittle Here</p>
  <p class="lorem" style="left:50px;top:192px;width:82px">Data trust is now a core need for every digital business.</p>
  <p class="head" style="left:159px;top:184px">Text Tittle Here</p>
  <p class="lorem" style="left:159px;top:192px;width:82px">Security tools shape how firms share and protect data.</p>
  <p class="head" style="left:270px;top:184px">Text Tittle Here</p>
  <p class="lorem" style="left:270px;top:192px;width:82px">We back teams building that layer of trust for all.</p>
  <p class="url">www. dalq7.ch</p>
  <p class="pager">01 / 39<br>Welcome Slide</p>
</section>

<!-- Row 6 -->
<section class="slide" style="left:116px;top:1521px">
  <p class="logo logo-corner">DALQ7</p>
  <svg style="left:60px;top:48px" width="20" height="14" viewBox="0 0 20 14"><path d="M1 7 5 3l4 3 3-3 7 5-4 4-4-3-3 3z" fill="none" stroke="#333" stroke-width="1"/></svg>
  <div style="left:162px;top:38px;width:42px;height:42px;border-radius:50%;background:var(--red)"></div>
  <svg style="left:174px;top:50px" width="18" height="18" viewBox="0 0 18 18"><rect x="2" y="5" width="12" height="9" fill="none" stroke="#fff"/><path d="M6 5V2h10v9h-2" fill="none" stroke="#fff"/></svg>
  <p class="head" style="left:49px;top:90px">Text Tittle Here</p>
  <p class="lorem" style="left:49px;top:98px;width:95px">We help founders with strategy, hiring and their next funding round.</p>
  <p class="head" style="left:166px;top:90px">Text Tittle Here</p>
  <p class="lorem" style="left:166px;top:98px;width:95px">Our network opens doors to clients, partners and key investors.</p>
  <svg style="left:60px;top:157px" width="20" height="20" viewBox="0 0 20 20"><path d="M10 2 16 5v6l-6 3-6-3V5zM4 11l6 3 6-3M10 8v6" fill="none" stroke="#333"/></svg>
  <svg style="left:176px;top:158px" width="16" height="16" viewBox="0 0 16 16"><path d="M15 1 1 7l5 2 2 6z" fill="none" stroke="#333"/></svg>
  <p class="head" style="left:49px;top:195px">Text Tittle Here</p>
  <p class="lorem" style="left:49px;top:203px;width:95px">We guide teams on security, compliance and data trust standards.</p>
  <p class="head" style="left:166px;top:195px">Text Tittle Here</p>
  <p class="lorem" style="left:166px;top:203px;width:95px">We support launches into new markets across Europe and beyond.</p>
  <h2 class="title" style="left:284px;top:62px;font-size:17px">Our Service</h2>
  <p class="lorem" style="left:284px;top:92px;width:170px">We invest in Swiss tech startups and work side by side with founders so they can scale faster.</p>
  <div class="photo" role="img" aria-label="Group of colleagues reviewing work on a laptop" style="left:287px;top:138px;width:166px;height:88px;background:linear-gradient(135deg,#bfbab2,#8c6a55 50%,#d9d5cf)"></div>
  <p class="url">www. dalq7.ch</p>
  <p class="pager">01 / 39<br>Welcome Slide</p>
</section>

<section class="slide" style="left:619px;top:1521px">
  <h2 class="title" style="left:200px;top:12px;font-size:17px">Our Team</h2>
  <p class="logo logo-corner">DALQ7</p>
  <div class="photo" role="img" aria-label="Portrait of a smiling middle-aged man in a dark suit" style="left:60px;top:41px;width:86px;height:86px;background:linear-gradient(180deg,#ececec,#3a3a3a)"></div>
  <div class="photo" role="img" aria-label="Portrait of a woman in a yellow sweater" style="left:198px;top:41px;width:86px;height:86px;background:linear-gradient(180deg,#ececec,#e0a52e)"></div>
  <div class="photo" role="img" aria-label="Portrait of a young man in a black T-shirt" style="left:338px;top:41px;width:86px;height:86px;background:linear-gradient(180deg,#ececec,#262626)"></div>
  <p style="left:60px;top:140px;width:86px;text-align:center;font-size:5px;line-height:1.4">Teo Marlin<br><b style="font-size:3.8px;letter-spacing:.8px">TYPE DESIGNER</b></p>
  <p style="left:198px;top:140px;width:86px;text-align:center;font-size:5px;line-height:1.4">Lina Voss<br><b style="font-size:3.8px;letter-spacing:.8px">PHOTOGRAPHER</b></p>
  <p style="left:338px;top:140px;width:86px;text-align:center;font-size:5px;line-height:1.4">Rian Kessel<br><b style="font-size:3.8px;letter-spacing:.8px">SLIDE DESIGNER</b></p>
  <p class="lorem" style="left:60px;top:158px;width:86px;text-align:center">Partner with years of work in early stage venture funding.</p>
  <p class="lorem" style="left:198px;top:158px;width:86px;text-align:center">Leads brand, content and outreach for our portfolio.</p>
  <p class="lorem" style="left:338px;top:158px;width:86px;text-align:center">Builds decks and visual stories for every founder.</p>
  <p class="btn" style="left:60px;top:215px;width:85px;background:var(--ink)">TEXT TITTLE</p>
  <p class="btn" style="left:199px;top:215px;width:85px;background:var(--red)">TEXT TITTLE</p>
  <p class="btn" style="left:338px;top:215px;width:85px;background:var(--ink)">TEXT TITTLE</p>
  <p class="url">www. dalq7.ch</p>
  <p class="pager">01 / 39<br>Welcome Slide</p>
</section>

<!-- Row 7 -->
<section class="slide" style="left:116px;top:1809px">
  <div style="left:0;top:0;width:63px;height:137px;background:var(--dark)"></div>
  <div style="left:0;top:137px;width:63px;height:138px;background:var(--red)"></div>
  <p style="left:28px;top:45px;font-size:4.5px;color:#fff;writing-mode:vertical-rl;letter-spacing:1px">TEXT</p>
  <p style="left:28px;top:100px;font-size:7px;color:#fff">↓</p>
  <p style="left:28px;top:160px;font-size:7px;color:#fff">↑</p>
  <p style="left:27px;top:220px;font-size:4.5px;color:#fff;writing-mode:vertical-rl;transform:rotate(180deg)">www. dalq7.ch</p>
  <h2 class="title" style="left:204px;top:10px;font-size:17px">Our Team</h2>
  <p class="logo logo-corner">DALQ7</p>
  <p style="left:100px;top:37px;font-size:5px;font-weight:600">Text title here</p>
  <p style="left:100px;top:50px;font-size:4px;font-style:italic;line-height:1.5">California, 03/14/1990<br><span style="color:#888">Photographer</span></p>
  <p style="left:241px;top:53px;font-size:4.5px">01</p>
  <div style="left:100px;top:62px;width:145px;height:1px;background:#ccc"></div>
  <p class="lorem" style="left:100px;top:70px;width:80px">Guides founders through growth, hiring and funding.</p>
  <p style="left:100px;top:117px;font-size:5px;font-weight:600">Text title here</p>
  <p style="left:100px;top:130px;font-size:4px;font-style:italic;line-height:1.5">California, 03/14/1990<br><span style="color:#888">Photographer</span></p>
  <p style="left:241px;top:133px;font-size:4.5px">02</p>
  <div style="left:100px;top:142px;width:145px;height:1px;background:#ccc"></div>
  <p class="lorem" style="left:100px;top:150px;width:80px">Shapes brand and story for each portfolio company.</p>
  <p style="left:100px;top:196px;font-size:5px;font-weight:600">Text title here</p>
  <p style="left:100px;top:209px;font-size:4px;font-style:italic;line-height:1.5">California, 03/14/1990<br><span style="color:#888">Photographer</span></p>
  <p style="left:241px;top:212px;font-size:4.5px">03</p>
  <div style="left:100px;top:221px;width:145px;height:1px;background:#ccc"></div>
  <p class="lorem" style="left:100px;top:229px;width:80px">Designs decks and visuals that win investor trust.</p>
  <p style="left:286px;top:62px;font-size:4.5px;letter-spacing:.8px;line-height:1.4;text-align:center">TEXT TITTLE HERE<br><span style="font-size:4px;color:#888">Nora Fell</span></p>
  <p style="left:286px;top:139px;font-size:4.5px;letter-spacing:.8px;line-height:1.4;text-align:center">TEXT TITTLE HERE<br><span style="font-size:4px;color:#888">Samir Oden</span></p>
  <p style="left:286px;top:217px;font-size:4.5px;letter-spacing:.8px;line-height:1.4;text-align:center">TEXT TITTLE HERE<br><span style="font-size:4px;color:#888">Elin Brandt</span></p>
  <div class="photo" role="img" aria-label="Portrait of a smiling man in a suit" style="left:352px;top:11px;width:72px;height:72px;background:linear-gradient(180deg,#f0f0f0,#3d3d3d)"></div>
  <div class="photo" role="img" aria-label="Portrait of a woman in a yellow sweater" style="left:352px;top:99px;width:72px;height:72px;background:linear-gradient(180deg,#f0f0f0,#e3a42c)"></div>
  <div class="photo" role="img" aria-label="Portrait of a young man in black" style="left:352px;top:188px;width:72px;height:72px;background:linear-gradient(180deg,#f0f0f0,#2a2a2a)"></div>
</section>

<section class="slide" style="left:619px;top:1809px">
  <div class="photo" role="img" aria-label="Grey perspective view of a modern building facade" style="inset:0;background:linear-gradient(115deg,#8c8c8c,#595959 45%,#3e3e3e 80%,#5a5a5a)"></div>
  <h2 style="left:0;width:491px;top:70px;text-align:center;font-family:Poppins,sans-serif;font-weight:500;font-size:70px;color:#fff;letter-spacing:1px">Breakslide</h2>
  <p style="left:0;width:491px;top:161px;text-align:center;font-size:7px;color:#ddd">Simple Presentation Template</p>
  <div class="dots" style="left:226px;top:210px"><span></span><span class="on"></span><span></span></div>
  <p style="left:24px;top:256px;font-size:5px;font-weight:600;color:#fff">www. dalq7.ch</p>
  <p style="right:16px;bottom:11px;font-size:5px;color:#fff;letter-spacing:.5px">TRUST <span style="display:inline-block;width:40px;border-top:1px solid #fff;vertical-align:middle;margin:0 6px"></span> ECONOMY</p>
</section>

<!-- Row 8 -->
<section class="slide" style="left:116px;top:2097px">
  <div class="photo" role="img" aria-label="Hands sketching charts on paper at a desk" style="left:0;top:0;width:176px;height:275px;background:linear-gradient(160deg,#7a6a5e,#d9d3cc 45%,#a7b2c7 80%,#e9e9e9)"></div>
  <div class="photo" role="img" aria-label="Business handshake over a city skyline" style="left:280px;top:0;width:211px;height:221px;background:linear-gradient(200deg,#d6dde6,#eaf0f6 40%,#7e97b3 85%)"></div>
  <div style="left:370px;top:221px;width:121px;height:54px;background:var(--red)"></div>
  <p style="left:392px;top:233px;font-size:6px;color:#fff">Text Tittle Here</p>
  <p class="lorem" style="left:392px;top:244px;width:80px;color:#fde">Joint projects with our partners.</p>
  <p style="left:24px;top:254px;font-size:4.5px;color:#eee">www. dalq7.ch</p>
  <p class="kicker" style="left:220px;top:136px;font-size:4.5px">Our Portfolio</p>
  <h2 class="title" style="left:220px;top:144px;font-size:17px;line-height:1.2">Our Project<br>Collaboration</h2>
  <p class="head" style="left:220px;top:210px">Text Tittle Here</p>
  <p class="lorem" style="left:220px;top:218px;width:90px">We co-build with founders and partner firms on real projects.</p>
</section>

<section class="slide" style="left:619px;top:2097px">
  <p class="kicker" style="left:38px;top:78px;font-size:4.5px">Mockup Device</p>
  <h2 class="title" style="left:38px;top:84px;font-size:17px">Tahu Dekstop</h2>
  <div style="left:38px;top:110px;width:80px;height:1px;background:var(--ink)"></div>
  <p class="head" style="left:38px;top:129px">Text Tittle Here</p>
  <p class="lorem" style="left:38px;top:137px;width:140px">Show your slides on any screen with a clean, simple device frame.</p>
  <svg style="left:225px;top:53px" width="210" height="170" viewBox="0 0 210 170">
    <rect x="1" y="1" width="208" height="138" rx="5" fill="#1a1a1a"/>
    <rect x="6" y="6" width="198" height="118" fill="#f2f2f2"/>
    <rect x="1" y="124" width="208" height="15" fill="#e4e4e4"/>
    <path d="M88 139h34l4 24H84z" fill="#cfcfcf"/>
    <rect x="68" y="162" width="74" height="4" rx="2" fill="#bdbdbd"/>
  </svg>
  <div class="photo" role="img" aria-label="Slide preview with a snowy mountain" style="left:238px;top:68px;width:184px;height:96px;background:linear-gradient(180deg,#4a5560,#9aa7b2 70%,#e3e8ec)"></div>
  <p style="left:238px;top:94px;width:184px;text-align:center;font-family:Poppins,sans-serif;font-weight:800;font-size:10px;line-height:1.1;color:#fff">ACCELERATE THE<br>ECONOMY OF TRUST</p>
  <p class="logo" style="left:238px;top:121px;width:184px;text-align:center;color:#fff;font-size:11px">DALQ7</p>
  <p class="url">www. dalq7.ch</p>
  <p class="pager">01 / 39<br>Welcome Slide</p>
</section>

<!-- Row 9 -->
<section class="slide" style="left:116px;top:2385px">
  <h2 class="title" style="left:22px;top:14px;font-size:17px">Europe <em>Map</em></h2>
  <p class="lorem" style="left:22px;top:40px;width:150px;font-size:5px">Lorem Ipsum has been the industry's standard dummy text ever since the 1500s.</p>
  <p style="left:22px;top:85px;font-size:8px;line-height:1.2">Write Your<br>Subtitle Here</p>
  <p class="lorem" style="left:22px;top:111px;width:115px">We support founders in every major hub across Europe, from Zurich to Berlin and Paris.</p>
  <p class="logo logo-corner">DALQ7</p>
  <div class="photo" role="img" aria-label="Grey map of Europe with Switzerland marked in red" style="left:220px;top:20px;width:271px;height:200px;background:radial-gradient(ellipse at 60% 55%,#c9c9c9 0%,#dedede 55%,#f6f6f6 80%,#fff 100%)"></div>
  <div style="left:18px;top:193px;width:22px;height:46px;background:var(--red)"></div>
  <div style="left:40px;top:193px;width:75px;height:46px;border:1px solid #e2e2e2"></div>
  <p style="left:54px;top:197px;font-size:10px;color:var(--red)">547M</p>
  <p class="lorem" style="left:54px;top:214px;width:55px">Share of users in the female group.</p>
  <div style="left:120px;top:193px;width:22px;height:46px;background:#999"></div>
  <div style="left:142px;top:193px;width:75px;height:46px;border:1px solid #e2e2e2"></div>
  <p style="left:155px;top:197px;font-size:10px;color:#888">457M</p>
  <p class="lorem" style="left:155px;top:214px;width:55px">Share of users in the male group.</p>
  <svg style="left:24px;top:207px" width="10" height="16" viewBox="0 0 10 16"><circle cx="5" cy="2.5" r="2.2" fill="#fff"/><path d="M5 5 1 12h8z" fill="#fff"/></svg>
  <svg style="left:126px;top:207px" width="10" height="16" viewBox="0 0 10 16"><circle cx="5" cy="2.5" r="2.2" fill="#fff"/><rect x="2.5" y="5.5" width="5" height="10" fill="#fff"/></svg>
  <p class="url">www. dalq7.ch</p>
  <p class="pager">01 / 39<br>Welcome Slide</p>
</section>

<section class="slide" style="left:619px;top:2385px">
  <h2 class="title" style="left:45px;top:22px;font-size:21px">Financials <em>Facts</em></h2>
  <p class="logo logo-corner">DALQ7</p>
  <table class="fin" style="left:43px;top:66px;width:408px">
    <tr><th>Editable Text</th><th>Editable Text</th><th>Editable Text</th><th>Editable Text</th><th>Editable Text</th><th>Editable Text</th></tr>
    <tr style="background:#f3f3f3"><td style="height:24px"></td><td style="color:var(--red);font-size:8px">✕</td><td style="color:var(--red);font-size:8px">◯</td><td style="color:var(--red);font-size:8px">▢</td><td style="color:var(--red);font-size:8px">◎</td><td style="color:var(--red);font-size:8px">⌂</td></tr>
    <tr><td class="rowlbl">Text Here</td><td>Text Here</td><td>Text Here</td><td>Text Here</td><td>Text Here</td><td>Text Here</td></tr>
    <tr><td class="rowlbl">Text Here</td><td>Text Here</td><td>Text Here</td><td>Text Here</td><td>Text Here</td><td>Text Here</td></tr>
    <tr><td class="rowlbl">Text Here</td><td>Text Here</td><td>Text Here</td><td>Text Here</td><td>Text Here</td><td>Text Here</td></tr>
    <tr><td class="rowlbl">Text Here</td><td>Text Here</td><td>Text Here</td><td>Text Here</td><td>Text Here</td><td>Text Here</td></tr>
    <tr><td class="rowlbl">Text Here</td><td>Text Here</td><td>Text Here</td><td>Text Here</td><td>Text Here</td><td>Text Here</td></tr>
    <tr><td class="rowlbl">Text Here</td><td>Text Here</td><td>Text Here</td><td>Text Here</td><td>Text Here</td><td>Text Here</td></tr>
    <tr><td class="rowlbl">Text Here</td><td>Text Here</td><td>Text Here</td><td>Text Here</td><td>Text Here</td><td>Text Here</td></tr>
  </table>
  <p class="url">www. dalq7.ch</p>
</section>

<!-- Row 10 -->
<section class="slide" style="left:116px;top:2673px">
  <h2 class="title" style="left:45px;top:34px;font-size:21px">Cash Flow <em>Forecast</em></h2>
  <p class="logo logo-corner">DALQ7</p>
  <div style="left:43px;top:78px;width:88px;height:160px;background:#f2f2f2"></div>
  <div style="left:43px;top:110px;width:88px;height:32px;background:#fde5e5"></div>
  <div style="left:43px;top:174px;width:88px;height:32px;background:#fde5e5"></div>
  <p style="left:48px;top:85px;font-size:4.5px;font-weight:700;line-height:1.5">Creative Proposal<br><span style="font-weight:400;color:#888">Plan for the first year</span></p>
  <p style="left:48px;top:117px;font-size:4.5px;font-weight:700">Creative Proposal</p>
  <p style="left:48px;top:149px;font-size:4.5px;font-weight:700">Creative Proposal</p>
  <p style="left:48px;top:181px;font-size:4.5px;font-weight:700;line-height:1.5">Creative Proposal<br><span style="font-weight:400;color:#888">Plan for the next year</span></p>
  <p style="left:48px;top:213px;font-size:4.5px;font-weight:700">Creative Proposal</p>
  <table class="cash" style="left:156px;top:78px;width:294px">
    <tr><th style="background:var(--ink)">2020</th><th style="background:var(--red)">2021</th><th style="background:var(--ink)">2022</th><th style="background:var(--red)">2023</th></tr>
    <tr><td>$ 450.00</td><td>$ 200.00</td><td>$ 150.00</td><td>$ 400.00</td></tr>
    <tr><td>Cash Flow</td><td>Cash Flow</td><td>Cash Flow</td><td>Cash Flow</td></tr>
    <tr><td>$ 1000.00</td><td>$ 2000.00</td><td>$ 3000.00</td><td>$ 2000.00</td></tr>
    <tr><td>$ 100.00</td><td>$ 200.00</td><td>$ 100.00</td><td>$ 150.00</td></tr>
    <tr><td>$ 100.00</td><td>$ 200.00</td><td>$ 200.00</td><td>$ 120.00</td></tr>
    <tr><td style="height:62px"></td><td></td><td></td><td></td></tr>
    <tr><td>Cash Flow</td><td>Cash Flow</td><td>Cash Flow</td><td>Cash Flow</td></tr>
  </table>
  <svg style="left:156px;top:176px" width="294" height="50" viewBox="0 0 294 50">
    <g fill="none" stroke-width="2.4">
      <circle cx="37" cy="25" r="14" stroke="#e6e6e6"/><path d="M37 11a14 14 0 0 1 14 14" stroke="var(--ink)"/>
      <circle cx="110" cy="25" r="14" stroke="#e6e6e6"/><path d="M110 11a14 14 0 0 1 8.2 25.3" stroke="var(--red)"/>
      <circle cx="184" cy="25" r="14" stroke="#e6e6e6"/><path d="M184 11a14 14 0 0 1 11.3 22.2" stroke="var(--ink)"/>
      <circle cx="257" cy="25" r="14" stroke="#e6e6e6"/><path d="M257 11a14 14 0 0 1 14 14" stroke="var(--red)"/>
    </g>
    <g font-size="4.5" font-family="Montserrat,sans-serif" text-anchor="middle" fill="#333">
      <text x="37" y="27">25%</text><text x="110" y="27">40%</text><text x="184" y="27">35%</text><text x="257" y="27">25%</text>
    </g>
  </svg>
  <p class="url">www. dalq7.ch</p>
</section>

</body>
</html>
```